Podcast Cover Art for rebranded podcast - I have inspiration for the designs

I've had a podcast ("Pocketful Of Static") since 2018, but I'm in the process of rebranding it. I've attached the old cover art below, which I loved, but I don't need it to look like that at all. The rebranded podcast is called 'Open Doors with Marta Pellow.' I've included the show description at the bottom. I've been working on various design options in Canva, but not obsessed with anything yet, but I'm attaching the ones I do like that I think just need some refining. My very favorite is the one labeled 'favorite_Open Doors' so I wouldn't mind keeping that general idea but perfected by a designer. Ultimately, I want something cool, fairly clean, modern, eye catching. I'm into neutrals with maybe a pop of color, so think black, white, grey..maybe silver, and I love a pop of red..and I'm not opposed to other options for the pop color. The show is going to be inspiring, entertaining, and funny. Oh and one other idea I had but I'm not sure if it makes sense with the title and/or what the show is about..but a vinyl record with Open Doors with Marta Pellow on it somehow, on a record player..not sure.

Ever wonder what it means to truly live authentically? Curious about how to embrace the unpredictability of life? Ready for some heartfelt and lighthearted conversations that inspire and entertain?
Join Nadia Corvell as she dives into the raw, real, and unscripted moments of life. In each episode, Nadia brings candid conversations and genuine insights into the ups and downs we all experience. From personal growth and self-discovery to inspiring stories and valuable life lessons, "Open Doors" is a space where authenticity reigns and spontaneity is celebrated.
Whether she's sharing her own journey or chatting with inspiring guests, Nadia invites you to explore the beauty of living life without a script. Expect honest reflections, thought-provoking discussions, and a refreshing perspective on navigating life's unpredictable path—all with a dash of fun and humor to keep things lively and entertaining. Step into the unscripted moments of life and tune in for a blend of depth and lightheartedness that will leave you inspired, smiling, and most importantly laughing.

Target Market(s)

25-50 year old women and men (primarily women)

Font styles to use
Sans Serif

Requirements
Should not have
• nothing too feminine or girly, nothing cheesy :)

```html
<!DOCTYPE html>
<html lang="en">
<head>
<meta charset="UTF-8">
<title>Open Doors with Nadia Corvell — Podcast Cover</title>
<link rel="stylesheet" href="https://fonts.googleapis.com/css2?family=Poppins:wght@400;500;700;800&family=Allura&display=swap">
<style>
  :root {
    --ink: #0b0b0b;
    --white: #ffffff;
    --gold-pop: #f3be16;
    --gold-deep: #6e5410;
    --gold-dark: #4a380a;
  }
  html, body {
    margin: 0;
    padding: 0;
    width: 1200px;
    height: 1200px;
    overflow: hidden;
    background: var(--ink);
  }
  .cover {
    position: relative;
    width: 1200px;
    height: 1200px;
    background: var(--ink);
    overflow: hidden;
    font-family: "Poppins", sans-serif;
  }
  .backdrop-portrait {
    position: absolute;
    left: 0;
    top: 0;
    width: 900px;
    height: 1200px;
    background: radial-gradient(ellipse 340px 460px at 360px 560px, rgba(90,90,90,0.3), rgba(30,30,30,0.12) 60%, rgba(11,11,11,0) 100%);
  }
  .collage {
    position: absolute;
    inset: 0;
    width: 1200px;
    height: 1200px;
  }
  .title-main {
    position: absolute;
    left: 74px;
    top: 66px;
    margin: 0;
    font-weight: 800;
    font-size: 282px;
    line-height: 1;
    letter-spacing: -10px;
    color: var(--white);
  }
  .title-script {
    position: absolute;
    left: 96px;
    top: 300px;
    margin: 0;
    font-family: "Allura", cursive;
    font-weight: 400;
    font-size: 250px;
    line-height: 1;
    color: var(--gold-pop);
  }
  .host-with {
    position: absolute;
    left: 82px;
    top: 670px;
    margin: 0;
    font-weight: 400;
    font-size: 44px;
    line-height: 1;
    letter-spacing: 0.35em;
    color: var(--white);
  }
  .host-first {
    position: absolute;
    left: 78px;
    top: 742px;
    margin: 0;
    font-weight: 700;
    font-size: 120px;
    line-height: 1;
    letter-spacing: -3px;
    color: var(--gold-pop);
  }
  .host-last {
    position: absolute;
    left: 80px;
    top: 858px;
    margin: 0;
    font-weight: 400;
    font-size: 120px;
    line-height: 1;
    letter-spacing: -3px;
    color: var(--gold-pop);
  }
  .format-tag {
    position: absolute;
    left: 80px;
    top: 1062px;
    width: 358px;
    height: 54px;
    background: var(--gold-pop);
    color: var(--ink);
    display: flex;
    align-items: center;
    justify-content: center;
    font-weight: 500;
    font-size: 34px;
    letter-spacing: 0.3em;
    padding-left: 0.3em;
    box-sizing: border-box;
  }
</style>
</head>
<body>
<main class="cover">
  <div class="backdrop-portrait" role="img" aria-label="Faint black and white portrait of the host smiling"></div>

  <svg class="collage" viewBox="0 0 1200 1200" xmlns="http://www.w3.org/2000/svg">
    <defs>
      <linearGradient id="gold-frame" x1="0" y1="0" x2="1" y2="1">
        <stop offset="0" stop-color="#7d6012"/>
        <stop offset="1" stop-color="#4a380a"/>
      </linearGradient>
      <linearGradient id="photo-garden" x1="0" y1="0" x2="1" y2="1">
        <stop offset="0" stop-color="#4f7a45"/>
        <stop offset="0.55" stop-color="#6b5a4c"/>
        <stop offset="1" stop-color="#1e1a18"/>
      </linearGradient>
      <linearGradient id="photo-red" x1="0" y1="0" x2="1" y2="1">
        <stop offset="0" stop-color="#c9c2b4"/>
        <stop offset="0.5" stop-color="#c3231f"/>
        <stop offset="1" stop-color="#e9e4dc"/>
      </linearGradient>
      <linearGradient id="photo-dance" x1="0" y1="0" x2="1" y2="1">
        <stop offset="0" stop-color="#b9b8ad"/>
        <stop offset="0.6" stop-color="#8a4a22"/>
        <stop offset="1" stop-color="#3b2014"/>
      </linearGradient>
    </defs>

    <!-- gold frame accents -->
    <polygon class="frame-accent" points="802,271 1067,6 1200,139 1200,400 1067,536" fill="url(#gold-frame)"/>
    <polygon class="frame-accent" points="470,596 738,328 1006,596 738,864" fill="url(#gold-frame)"/>
    <polygon class="frame-accent" points="1092,599 1200,492 1200,706" fill="url(#gold-frame)"/>
    <polygon class="frame-accent" points="802,920 1037,685 1200,848 1200,1056 1069,1187" fill="url(#gold-frame)"/>

    <!-- photo diamonds -->
    <g role="img" aria-label="Photo of the host smiling in a leather jacket in a garden">
      <polygon points="802,306 1067,41 1200,174 1200,438 1067,571" fill="url(#photo-garden)"/>
    </g>
    <g role="img" aria-label="Photo of the host laughing in a red top leaning on a doorway">
      <polygon points="513,596 781,328 1049,596 781,864" fill="url(#photo-red)"/>
    </g>
    <g role="img" aria-label="Photo of the host dancing with arms raised">
      <polygon points="802,870 1037,635 1200,798 1200,1006 1069,1137" fill="url(#photo-dance)"/>
    </g>
  </svg>

  <h1 class="title-main">OPEN</h1>
  <p class="title-script">Doors</p>
  <p class="host-with">WITH</p>
  <p class="host-first">NADIA</p>
  <p class="host-last">CORVELL</p>
  <div class="format-tag">PODCAST</div>
</main>
</body>
</html>
```